Professional business cards for real estate development company

I need business cards for my new real estate development company. The company, "KORVA" is a real estate development, investment, and advisory firm with a focus on multifamily, office, and mixed-use projects across primary and secondary markets in the Southeast United States.

Style preference is modern

Industry/Entity Type

Real Estate Development

Contact Information for Business Card

The business cards need to include:
Name
Title
Mailing Address
Phone Number
Web Address

Logo is attached. I would like white to be the primary color with incorporation of the company colors: #232D3A and #B5A451

Font styles to use
Other font styles liked:
• Montserrat, Avenir

Requirements
Must have
• Company Logo. No need to include the company name since the name is in the logo.
Should not have
• No line type designs

```html
<!DOCTYPE html>
<html lang="en">
<head>
<meta charset="utf-8">
<title>KORVA Business Card</title>
<link href="https://fonts.googleapis.com/css2?family=Montserrat:ital,wght@0,400;0,600;0,700;1,400;1,600;1,700;1,800&display=swap" rel="stylesheet">
<style>
  :root {
    --navy: #232D3A;
    --gold: #B5A451;
    --white: #FFFFFF;
    --stage: #3A3A3A;
    --sky-slate: #5A6778;
    --sky-rose: #9C7A72;
    --sky-sand: #C9A96A;
  }
  * { margin: 0; padding: 0; box-sizing: border-box; }
  html, body { width: 1200px; height: 720px; overflow: hidden; }
  body {
    background: var(--stage);
    font-family: "Montserrat", Arial, sans-serif;
    position: relative;
  }
  .card {
    position: absolute;
    left: 351px;
    width: 525px;
    height: 300px;
    background: var(--white);
    overflow: hidden;
  }
  .card--front { top: 22px; }
  .card--back { top: 398px; }

  .wordmark {
    position: absolute;
    display: flex;
    align-items: center;
    gap: 10px;
    color: var(--navy);
    font-weight: 700;
    letter-spacing: 0.08em;
    white-space: nowrap;
  }
  .wordmark__square {
    width: 0.55em;
    height: 0.55em;
    background: var(--navy);
    flex: none;
  }
  .card--front .wordmark {
    left: 0; right: 0; top: 50px;
    justify-content: center;
    font-size: 58px;
  }
  .skyline {
    position: absolute;
    left: 0; right: 0; bottom: 0;
    height: 142px;
    background: linear-gradient(90deg, var(--sky-slate) 0%, var(--sky-rose) 30%, var(--sky-sand) 45%, var(--sky-rose) 60%, var(--sky-slate) 80%, var(--navy) 100%);
    opacity: 0.55;
  }

  .holder { position: absolute; left: 46px; top: 34px; color: var(--navy); }
  .holder__name { font-size: 34px; line-height: 1; white-space: nowrap; }
  .holder__first { font-weight: 400; margin-right: 22px; }
  .holder__last { font-weight: 800; font-style: italic; }
  .holder__title {
    margin: 14px 0 0 26px;
    font-size: 22px; font-weight: 700; font-style: italic;
  }
  .card--back .wordmark {
    left: 358px; top: 58px;
    font-size: 28px;
    gap: 8px;
    letter-spacing: 0.06em;
  }

  .contact-band {
    position: absolute;
    left: 0; right: 0; top: 150px; bottom: 0;
    background: var(--navy);
    border-top: 3px solid var(--gold);
  }
  .contact-list { list-style: none; position: absolute; left: 12px; top: 0; }
  .contact-list li {
    display: flex; align-items: center;
    height: 37px;
    color: var(--gold);
    font-size: 16px;
    white-space: nowrap;
  }
  .contact-list svg { width: 18px; height: 18px; margin-right: 14px; flex: none; }
  .contact-list .phone { font-style: italic; }

  .values { position: absolute; left: 348px; top: 134px; display: flex; gap: 4px; }
  .value { width: 37px; text-align: center; color: var(--gold); font-size: 8.5px; font-weight: 700; font-style: italic; }
  .value__dot {
    display: block; width: 12px; height: 12px; margin: 0 auto 7px;
    border: 1.4px solid var(--navy); border-radius: 50%; background: var(--white);
  }
  .towers {
    position: absolute; left: 384px; top: 25px; right: 10px; bottom: 0;
    background: linear-gradient(180deg, var(--gold), #8E8140);
    opacity: 0.85;
  }
</style>
</head>
<body>
  <section class="card card--front">
    <div class="wordmark"><span class="wordmark__square"></span>KORVA</div>
    <div class="skyline" role="img" aria-label="City skyline illustration of high-rise buildings in slate, rose and sand tones"></div>
  </section>

  <section class="card card--back">
    <div class="holder">
      <p class="holder__name"><span class="holder__first">Daniel</span><span class="holder__last">Hale</span></p>
      <p class="holder__title">Sales Manager</p>
    </div>
    <div class="wordmark"><span class="wordmark__square"></span>KORVA</div>

    <div class="contact-band">
      <ul class="contact-list">
        <li class="phone">
          <svg viewBox="0 0 24 24" fill="var(--gold)"><path d="M6.6 10.8a15 15 0 0 0 6.6 6.6l2.2-2.2a1 1 0 0 1 1-.25 11.4 11.4 0 0 0 3.6.57 1 1 0 0 1 1 1V20a1 1 0 0 1-1 1A17 17 0 0 1 3 4a1 1 0 0 1 1-1h3.5a1 1 0 0 1 1 1c0 1.250.2 2.450.57 3.6a1 1 0 0 1-.25 1z"/></svg>
          +1 000-000-0042
        </li>
        <li>
          <svg viewBox="0 0 24 24" fill="none" stroke="var(--gold)" stroke-width="2"><rect x="3" y="5" width="18" height="14" rx="1"/><path d="M3 6l9 7 9-7"/></svg>
          info@korvadevelopment.com
        </li>
        <li>
          <svg viewBox="0 0 24 24" fill="none" stroke="var(--gold)" stroke-width="1.8"><circle cx="12" cy="12" r="9"/><path d="M3 12h18M12 3c3 3 3 15 0 18M12 3c-3 3-3 15 0 18"/></svg>
          www.korvadevelopment.com
        </li>
        <li>
          <svg viewBox="0 0 24 24" fill="none" stroke="var(--gold)" stroke-width="2"><path d="M12 22s7-7 7-12a7 7 0 0 0-14 0c0 5 7 12 7 12z"/><circle cx="12" cy="10" r="2.5"/></svg>
          418 Alder Crest NE Atlanta, GA 30309
        </li>
      </ul>
      <div class="towers" role="img" aria-label="Gold illustration of two office towers"></div>
    </div>

    <div class="values">
      <div class="value"><span class="value__dot"></span>Reliance</div>
      <div class="value"><span class="value__dot"></span>Trust</div>
      <div class="value"><span class="value__dot"></span>Loyalty</div>
      <div class="value"><span class="value__dot"></span>Honesty</div>
    </div>
  </section>
</body>
</html>
```